Electrical contractor

looking for a standard sized, horizontal, double sided business card for an electrical contractors business.
i have played around on microsoft word (only computer program i know how to use!) and will attach what i have made so far, really open to any ideas. i just want the DORB to stand out to the rest of the business name.

i wish to use the colours black and green, and white for writing. i will attach the pictures i took off google, i want to either use them, or somethin similar for the back grounds

i wish the front to have the following info:
business name: D.O.R.B ELECTRICAL CONTRACTORS
MY NAME; CORBIN HOLT
STATUS; A CLASS ELECTRICIAN
LICENSE NO; TRN517394
PH NO. 0431576204
EMAIL ADD. DORB.ELECTRICAL@VELTOMAIL.COM
AND MY SLOGAN: where excellence meets integrity, and service comes with a smile.

i am not sure what to have on the back, other than what i do for work.eg titled WHAT WE DO
i dont want too much written on there or will look crowded, but options to add to back, from most important to least, please pick however many you think will look the best
new homes/extentions
led lighting and downlights
Solar Power
power
safety switches
switchboards
telephone and tv
smoke alarms
stoves and ovens
hot water systems
fault finding
re wiring
Updates

Thank you to those who have submitted designs, I would like to change my slogan to something more simple, I'm thinking something like. RELIABLE. EFFICIENT. PROFESSIONAL. AFFORDABLE. in what ever order you thinks fits best. Thanks

Industry/Entity Type

Contractor

```html
<!DOCTYPE html>
<html lang="en">
<head>
<meta charset="utf-8">
<title>D.O.R.B Electrical Contractors – Business Card</title>
<link rel="stylesheet" href="https://fonts.googleapis.com/css2?family=Lato:wght@400;700&display=swap">
<style>
  :root {
    --page-bg: #e7e3dd;
    --card-dark: #141414;
    --card-mid: #2c2c2c;
    --glow-green: #3fd43a;
    --glow-deep: #0f5a12;
    --text-silver: #d9d9d6;
    --text-soft: #c9c4bb;
    --text-white: #f2f2ee;
  }
  html, body {
    margin: 0;
    width: 1200px;
    height: 970px;
    overflow: hidden;
    background: var(--page-bg);
  }
  .canvas {
    position: relative;
    width: 1200px;
    height: 970px;
  }
  .business-card {
    position: absolute;
    left: 172px;
    top: 248px;
    width: 856px;
    height: 474px;
    overflow: hidden;
    background: linear-gradient(135deg, var(--card-mid) 0%, var(--card-dark) 55%, #1e1e1e 100%);
    box-shadow: 0 10px 30px rgba(0,0,0,0.25);
    font-family: "Lato", sans-serif;
    text-align: center;
  }
  .card-glow {
    position: absolute;
    left: 0; top: 0;
    width: 100%; height: 100%;
    background: radial-gradient(ellipse 300px 230px at 420px 205px, rgba(63,212,58,0.55) 0%, rgba(30,120,28,0.28) 40%, rgba(0,0,0,0) 75%);
  }
  .bulb-image {
    position: absolute;
    left: 310px;
    top: 108px;
    width: 210px;
    height: 330px;
    border-radius: 50% 50% 30% 30% / 38% 38% 20% 20%;
    background: radial-gradient(ellipse at 50% 30%, rgba(150,240,120,0.75) 0%, var(--glow-green) 25%, var(--glow-deep) 65%, rgba(20,40,20,0.4) 100%);
    opacity: 0.85;
  }
  .card-text {
    position: absolute;
    left: 0;
    width: 100%;
    margin: 0;
    color: var(--text-silver);
    letter-spacing: 0.5px;
  }
  .business-name { top: 38px; font-size: 29px; font-weight: 400; }
  .license-number { top: 73px; font-size: 16px; }
  .holder-name { top: 142px; font-size: 29px; font-weight: 700; color: var(--text-white); }
  .holder-status { top: 185px; font-size: 24px; color: var(--text-soft); }
  .phone-number { top: 258px; font-size: 24px; font-weight: 700; color: var(--text-white); }
  .email-address { top: 291px; font-size: 24px; color: var(--text-white); }
  .slogan { top: 355px; font-size: 22px; color: var(--text-soft); letter-spacing: 0.2px; }
</style>
</head>
<body>
<div class="canvas">
  <section class="business-card">
    <div class="card-glow"></div>
    <div class="bulb-image" role="img" aria-label="Glowing green light bulb photograph"></div>
    <p class="card-text business-name">D.O.R.B ELECTRICAL CONTRACTORS</p>
    <p class="card-text license-number">LICENSE NO; TRN517394</p>
    <p class="card-text holder-name">CORBIN HOLT</p>
    <p class="card-text holder-status">A CLASS ELECTRICIAN</p>
    <p class="card-text phone-number">0431576204</p>
    <p class="card-text email-address">DORB.ELECTRICAL@VELTOMAIL.COM</p>
    <p class="card-text slogan">“where excellence meets integrity, and service comes with a smile”</p>
  </section>
</div>
</body>
</html>
```